Law Firm Website

We are looking to update our old, tired and very flat website. We have someone who will code and host the site but we need some design inspiration. The website will consist of no more than 2/3 pages, possibly with pop-ups for information. We already have all the blurb. We would like something distinctive, clean and eye-catching, using the purple and white theme that we already use on our firm stationery. Examples uploaded. Current website URL is www.dunmorewillett.example.

Industry/Entity Type

Law Firm

```html
<!DOCTYPE html>
<html lang="en">
<head>
<meta charset="utf-8">
<title>Dunmore &amp; Willett Solicitors</title>
<link href="https://fonts.googleapis.com/css2?family=Source+Sans+3:wght@400;600&family=Oswald:wght@400&family=Tinos&display=swap" rel="stylesheet">
<style>
:root{
  --purple:#5b4580;
  --purple-dark:#4a3870;
  --ink:#1f2a33;
  --body:#3a3a3a;
  --muted:#8a8a8a;
  --rule:#e6e6e6;
  --panel:#ececec;
  --footer:#1e1e1e;
  --white:#ffffff;
}
*{margin:0;padding:0;box-sizing:border-box}
html,body{width:941px;height:1200px;overflow:hidden;background:var(--white)}
body{position:relative;font-family:"Source Sans 3",Arial,sans-serif;color:var(--body)}
.abs{position:absolute}
/* header */
.brand{left:108px;top:26px;font-size:26px;font-weight:400;color:var(--purple);letter-spacing:.2px}
.nav{left:448px;top:41px;display:flex;gap:0;font-size:11px;color:var(--ink)}
.nav a{color:var(--ink);text-decoration:none;height:23px;line-height:23px;padding:0 9px;margin-right:9px}
.nav a.active{background:var(--purple);color:var(--white)}
/* hero */
.hero{left:0;top:95px;width:941px;height:335px;background:var(--purple)}
.hero-art{left:0;top:55px;width:550px;height:215px;border-radius:0 60px 60px 0;background:linear-gradient(100deg,#e8d8b0 0%,#b89a6a 35%,#6b2f24 60%,rgba(91,69,128,0) 100%);opacity:.85}
.hero-title{left:564px;top:78px;font-family:"Oswald",Arial Narrow,sans-serif;font-size:28px;line-height:38px;color:var(--white);letter-spacing:.2px}
.hero-sub{left:565px;top:170px;font-size:14px;line-height:18px;color:var(--white)}
.hero-arrow{top:240px;width:28px;height:28px;border-radius:50%;background:var(--white)}
/* content */
h2{font-family:"Source Sans 3",Arial,sans-serif;font-weight:600;font-size:16px;color:var(--ink)}
.copy{font-size:8.6px;line-height:14.5px;color:var(--body)}
.copy p{margin-bottom:14.5px}
.photo{background:linear-gradient(160deg,#b9c3cf,#6d7480)}
.photo.building{background:linear-gradient(180deg,#9fb6d6 0%,#c9c2b4 55%,#7d7466 100%)}
.photo.mono{background:linear-gradient(160deg,#4a4a4a,#cfcfcf)}
.btn{background:var(--purple);color:var(--white);font-size:9.5px;line-height:26px;padding:0 16px;width:78px}
.hr{height:1px;background:var(--rule)}
.vr{left:593px;top:470px;width:1px;height:635px;background:var(--rule)}
/* sidebar */
.search-input{left:622px;top:491px;width:173px;height:26px;background:var(--panel)}
.search-btn{left:804px;top:491px;width:28px;height:26px;background:var(--purple)}
.areas{left:622px;top:605px;list-style:none;font-family:"Tinos","Times New Roman",serif;font-size:7.6px;line-height:14.5px;color:var(--muted);text-transform:uppercase}
.areas li::before{content:">";display:inline-block;width:14px;padding-left:4px}
.quote{left:622px;top:923px;width:178px;height:81px;background:var(--panel);font-family:"Tinos","Times New Roman",serif;font-size:9.6px;line-height:11.5px;color:var(--ink);padding:14px 48px 0 30px}
.quote-name{left:641px;top:1019px;font-size:9.5px;font-weight:600;color:var(--purple)}
/* footer */
.footer{left:0;top:1106px;width:941px;height:94px;background:var(--footer);color:var(--white);font-size:9px}
.footer-links{left:112px;top:27px}
.footer-copy{left:112px;top:56px}
.social{top:28px;width:32px;height:32px;border-radius:50%;background:var(--purple)}
</style>
</head>
<body>
<header>
  <div class="abs brand">Dunmore &amp; Willett</div>
  <nav class="abs nav">
    <a class="active" href="#">Home</a><a href="#">Areas of Expertise</a><a href="#">Daniel Dunmore</a><a href="#">Peter Willett</a><a href="#">Contact</a>
  </nav>
</header>

<section class="abs hero">
  <div class="abs hero-art" role="img" aria-label="Law books, a wooden gavel and brass scales of justice"></div>
  <div class="abs hero-title">DUNMORE &amp; WILLETT SOLICITORS<br>FOR THE SERVICE YOU DESRVE</div>
  <div class="abs hero-sub">Sem iaculis blandit et nec&nbsp; sundre<br>tortor nullum sepur</div>
  <svg class="abs hero-arrow" style="left:587px" viewBox="0 0 28 28" aria-label="Previous slide"><path d="M16 8l-6 6 6 6" fill="none" stroke="#333" stroke-width="1.8"/></svg>
  <svg class="abs hero-arrow" style="left:616px" viewBox="0 0 28 28" aria-label="Next slide"><path d="M12 8l6 6-6 6" fill="none" stroke="#333" stroke-width="1.8"/></svg>
</section>

<main>
  <h2 class="abs" style="left:108px;top:458px">Welcome to Dunmore &amp; Willett Solicitors</h2>
  <div class="abs photo building" style="left:108px;top:502px;width:177px;height:181px" role="img" aria-label="Gothic court building exterior"></div>
  <div class="abs copy" style="left:314px;top:501px;width:255px">
    <p>&nbsp;High Court, LondonDUNMORE and WILLETT is a firm of solicitors with offices in Highgate, London and Hatfield, Hertfordshire.</p>
    <p>This firm is authorised and regulated by the Legal Standards Authority, no.731086.</p>
    <p>VAT registered number: 418 2097 36</p>
    <p>Professional rules can be viewed on www.legalstandards.example/conduct.page.</p>
  </div>
  <div class="abs btn" style="left:318px;top:657px">More Info</div>
  <div class="abs hr" style="left:108px;top:713px;width:458px"></div>

  <h2 class="abs" style="left:108px;top:734px">Daniel Dunmore</h2>
  <div class="abs photo" style="left:110px;top:781px;width:77px;height:88px" role="img" aria-label="Portrait of Daniel Dunmore"></div>
  <div class="abs copy" style="left:202px;top:779px;width:370px;line-height:16px">
    <p style="margin-bottom:16px">Daniel Dunmore qualified as a solicitor in 1987 and spent many years working with a busy commercial practice in North Middlesex.</p>
    <p>After taking a career break in the 1990's to work as a writer and media consultant, he return to the law in 2000 as a freelance advocate before setting up his own practice in 2002</p>
  </div>
  <div class="abs hr" style="left:108px;top:897px;width:458px"></div>

  <h2 class="abs" style="left:108px;top:913px">Peter Willett</h2>
  <div class="abs photo mono" style="left:108px;top:947px;width:102px;height:78px" role="img" aria-label="Black and white portrait of Peter Willett"></div>
  <div class="abs copy" style="left:223px;top:943px;width:345px;line-height:16px">
    <p style="margin-bottom:16px">Peter Willett has 40 years experience in the law.</p>
    <p style="margin-bottom:16px">He qualified in the City of London where he worked for many years and then set up his own firm in 1981 and then going on to join a larger commercial practice for 2 years.</p>
    <p>He has a wide range of expertise in commercial and private client matters</p>
  </div>

  <div class="abs vr"></div>
</main>

<aside>
  <h2 class="abs" style="left:622px;top:455px">Site Search Here</h2>
  <div class="abs search-input"></div>
  <svg class="abs search-btn" viewBox="0 0 28 26" aria-label="Search"><circle cx="12" cy="11" r="5" fill="none" stroke="#fff" stroke-width="2"/><path d="M15.5 14.5l5 5" stroke="#fff" stroke-width="2.6" stroke-linecap="round"/></svg>
  <div class="abs hr" style="left:622px;top:547px;width:210px"></div>

  <h2 class="abs" style="left:622px;top:573px">Main Areas of Expertise</h2>
  <ul class="abs areas">
    <li>Company Matters</li><li>Commercial Matters</li><li>Commercial Crime</li><li>Litigation/Disputes</li><li>Insolvency</li><li>Residential Conveyancing</li><li>Commercial Conveyancing</li><li>Wills &amp; Probate</li><li>Estate Planning</li><li>Powers of Attorney</li><li>Care of the Elderly</li><li>Court of Protection</li><li>Divorce/Family</li><li>Pre-Nuptial Agreements</li><li>Intellectual Property</li><li>Media Law</li>
  </ul>
  <div class="abs hr" style="left:622px;top:867px;width:210px"></div>

  <h2 class="abs" style="left:622px;top:892px">Testimonials</h2>
  <div class="abs quote">“Thank you, thank you, thank you. Your hard work and dedication has changed my life for the better”.</div>
  <svg class="abs" style="left:643px;top:1004px" width="14" height="9" viewBox="0 0 14 9"><path d="M0 0h14L6 9z" fill="#ececec"/></svg>
  <div class="abs quote-name">Jane Marsh</div>
</aside>

<footer class="abs footer">
  <div class="abs footer-links">Home&nbsp; | &nbsp;Areas of Expertise&nbsp; | &nbsp;Daniel Dunmore&nbsp; | &nbsp;Peter Willett&nbsp; | &nbsp;Contact</div>
  <div class="abs footer-copy">Copyright © Dunmore &amp; Willett. All rights reserved&nbsp; | &nbsp;Legal Notices |&nbsp; Privacy Policy</div>
  <div class="abs social" style="left:701px" role="img" aria-label="Social network link"></div>
  <div class="abs social" style="left:740px" role="img" aria-label="Social network link"></div>
  <div class="abs social" style="left:779px" role="img" aria-label="Social network link"></div>
</footer>
</body>
</html>
```